NEED A BUSINESS CARD FOR A NEW ELECTRICAL BUSINESS

HI I am after a new business card for my new electrical business I have a logo that I have attached its the one in blue, I would like that on the front and on the back my name- Marcus fell, Email marcusfell@tralvinet.com, mobile 0491570156, licence no# vic 48107, nsw 315042k I wont something that is a stand out from the rest but at the same time is neat as being a new business I wont it to catch peoples eye on the front of the card I would like the logo and not much else.
And on the back as well I would like a slogan saying something like
Quality-Reliable-Service

Hi all on the back of the card I would like a little slogan like Quality-Reliable-Service something like that would be good thanks

Hi all the business card needs to have both these licence numbers on it                                                  VIC-48107 nsw-315042k

```html
<!DOCTYPE html>
<html lang="en">
<head>
<meta charset="utf-8">
<title>Fellwire Electrical – Business Card</title>
<link rel="stylesheet" href="https://fonts.googleapis.com/css2?family=Arimo:wght@400;700&family=Noto+Serif:wght@700&display=swap">
<style>
  :root {
    --page: #ead7d9;
    --card-dark: #262626;
    --card-mid: #3a3a38;
    --blue: #1a84d2;
    --grey: #8b8d90;
    --grey-light: #b9bbbe;
    --name-grey: #9a9a9a;
  }
  * { box-sizing: border-box; margin: 0; padding: 0; }
  html, body { width: 1200px; height: 675px; overflow: hidden; }
  body {
    background: var(--page);
    font-family: "Arimo", Arial, sans-serif;
    position: relative;
  }
  .card {
    position: absolute;
    top: 187px;
    width: 525px;
    height: 300px;
    background: radial-gradient(ellipse at 70% 35%, var(--card-mid), var(--card-dark) 75%);
    overflow: hidden;
    box-shadow: 0 10px 24px rgba(80, 30, 40, .25);
  }
  .card--front { left: 50px; }
  .card--back { left: 625px; }

  .brand {
    position: absolute;
    display: flex;
    align-items: center;
    gap: 10px;
    color: var(--blue);
    font-weight: 700;
    letter-spacing: 1px;
  }
  .brand__square { width: 20px; height: 20px; background: var(--blue); }
  .card--front .brand { left: 0; right: 0; top: 88px; justify-content: center; font-size: 26px; }
  .card--back .brand { left: 50px; top: 26px; font-size: 20px; }
  .card--back .brand__square { width: 16px; height: 16px; }

  .decor { position: absolute; inset: 0; width: 100%; height: 100%; }

  .slogan {
    position: absolute;
    font-weight: 700;
    font-size: 15px;
    letter-spacing: .2px;
  }
  .card--front .slogan { right: 48px; top: 195px; color: var(--blue); }
  .card--back .slogan { right: 54px; top: 234px; color: var(--grey-light); }

  .contact { position: absolute; left: 50px; top: 82px; }
  .contact__name {
    font-family: "Noto Serif", Georgia, serif;
    font-weight: 700;
    font-size: 19px;
    color: var(--name-grey);
    margin-bottom: 10px;
  }
  .contact__line { font-size: 12px; color: var(--blue); line-height: 22px; }
</style>
</head>
<body>

<section class="card card--front" aria-label="Card front">
  <svg class="decor" viewBox="0 0 525 300" aria-hidden="true">
    <polyline points="0,135 180,135 200,160 525,160" fill="none" stroke="#8b8d90" stroke-width="1"/>
    <polyline points="0,222 340,222" fill="none" stroke="#8b8d90" stroke-width="1"/>
    <rect x="0" y="262" width="290" height="38" fill="#8b8d90"/>
    <rect x="290" y="262" width="235" height="38" fill="#1a84d2"/>
  </svg>
  <div class="brand"><span class="brand__square"></span>FELLWIRE ELECTRICAL</div>
  <p class="slogan">Quality-Reliable-Service</p>
</section>

<section class="card card--back" aria-label="Card back">
  <svg class="decor" viewBox="0 0 525 300" aria-hidden="true">
    <line x1="0" y1="200" x2="525" y2="200" stroke="#1a84d2" stroke-width="1"/>
    <line x1="0" y1="258" x2="525" y2="258" stroke="#1a84d2" stroke-width="1"/>
    <rect x="0" y="266" width="265" height="34" fill="#1a84d2"/>
    <rect x="265" y="266" width="260" height="34" fill="#8b8d90"/>
  </svg>
  <div class="brand"><span class="brand__square"></span>FELLWIRE ELECTRICAL</div>
  <div class="contact">
    <p class="contact__name">Marcus fell</p>
    <p class="contact__line">E: marcusfell@tralvinet.com</p>
    <p class="contact__line">M: 0491570156</p>
    <p class="contact__line">l. no:vic 48107</p>
    <p class="contact__line">nsw 315042k</p>
  </div>
  <p class="slogan">Quality-Reliable-Service</p>
</section>

</body>
</html>
```